Emergency Response Company Needs a Web Design

To go along with a completed logo redesign, we are looking to update and modernize the design and feel of our site.The emergency response planning we do is based around the oil and gas industry. Our existing site at http://www.corvanplan.example/ will give some insight in to what we do. For more related insight, here are some direct competitors:
http://www.tamrilguard.example/index.php
http://www.silverpinewrx.example/
http://quolvapower.example/
http://dervishltd.example/company.php
http://www.prime-rescue.example/

Industry/Entity Type

Oil And Gas

```html
<!DOCTYPE html>
<html lang="en">
<head>
<meta charset="utf-8">
<title>Corvan Resource Consultants Ltd.</title>
<link href="https://fonts.googleapis.com/css2?family=Mulish:wght@300;400;600&display=swap" rel="stylesheet">
<style>
:root{
  --red:#b3121e;
  --red-nav:#c8102e;
  --dark:#3b3b3b;
  --tile:#444;
  --text:#444;
  --line:#d6d6d6;
  --panel:#f3f3f3;
  --footer:#3d3d3d;
}
*{box-sizing:border-box;margin:0;padding:0}
html,body{width:1200px;height:1182px;overflow:hidden;background:#fff;font-family:"Mulish",sans-serif;color:var(--text)}
.page{position:relative;width:1200px;height:1182px}
.abs{position:absolute}
.brand{left:74px;top:34px;display:flex;align-items:center;gap:12px}
.brand-name{font-size:44px;font-weight:300;color:var(--dark);letter-spacing:1px;line-height:1}
.brand-sub{font-size:15px;font-weight:300;color:var(--dark);letter-spacing:.5px;margin-top:4px;border-top:1px solid var(--red);padding-top:3px}
.brand-mark{width:44px;height:44px;background:var(--red)}
.callus{right:73px;top:22px;font-size:17px;color:var(--dark);display:flex;align-items:center;gap:8px}
.callus b{font-weight:400;color:#222}.callus em{font-style:normal;color:var(--red)}
.nav{left:423px;top:67px;width:704px;height:39px;background:var(--red-nav);display:flex}
.nav a{color:#fff;text-decoration:none;font-size:13px;font-weight:600;display:flex;align-items:center;justify-content:center;flex:1}
.nav a.current{background:var(--dark);flex:0 0 88px}
.hero{left:74px;top:119px;width:1053px;height:372px;background:#ddd;padding:5px}
.hero-photo{width:100%;height:100%;background:linear-gradient(100deg,#5b5a63 0%,#8a8e99 30%,#b9c6d4 55%,#e3dfcf 100%);position:relative}
.hero-title{position:absolute;left:604px;top:148px;font-size:37px;line-height:37px;color:var(--red);font-weight:400}
.dots{position:absolute;right:37px;bottom:17px;display:flex;gap:11px}
.dots i{width:14px;height:14px;border-radius:2px;background:#1a1a1a}
.dots i.on{background:#fff}
h1{left:74px;top:512px;font-size:25px;font-weight:400;color:var(--red)}
.intro{left:74px;top:554px;width:790px;font-size:12.5px;line-height:21.3px}
.btn{background:var(--dark);color:#fff;font-size:12px;text-decoration:none;display:inline-flex;align-items:center;justify-content:center;height:34px;border-radius:2px}
.intro-btn{left:74px;top:661px;width:152px}
.rule{left:74px;top:713px;width:783px;height:1px;background:var(--line)}
.card{top:736px;width:243px;height:305px;background:var(--panel);border:1px solid var(--line);padding:15px}
.card-img{height:131px;border:1px solid #ccc}
.card h2{font-size:20px;font-weight:400;color:var(--red);margin-top:12px}
.card p{font-size:12.5px;line-height:18.5px;margin-top:4px}
.card .btn{width:96px;margin-top:17px}
.tile{left:884px;width:243px;height:95px;background:linear-gradient(#555,#3c3c3c);border-radius:2px;display:flex;align-items:center;padding-left:18px;gap:20px;color:#fff;font-size:23px;line-height:26px}
.tile svg{flex:0 0 58px}
.contact{left:884px;top:840px;width:243px;height:198px;background:var(--panel);border:1px solid var(--line);padding:14px 16px}
.contact h3{font-size:25px;font-weight:400;color:var(--red);line-height:30px}
.contact .org{font-size:13.5px;color:#222;line-height:18px;margin-top:3px}
.contact .addr{font-size:12.5px;line-height:19px}
.contact dl{display:grid;grid-template-columns:67px 1fr;font-size:12px;line-height:21px;margin-top:3px}
.contact dd{color:var(--red)}
.footer{left:0;top:1081px;width:1200px;height:101px;background:var(--footer);color:#ddd}
.foot-links{position:absolute;left:74px;top:22px;font-size:12px;word-spacing:2px}
.foot-links span{margin:0 10px}
.copy{position:absolute;left:74px;top:62px;font-size:11.5px;color:#bbb}
.social{position:absolute;left:958px;top:38px;display:flex;gap:7px}
.social i{width:30px;height:30px;border-radius:50%}
</style>
</head>
<body>
<div class="page">
  <div class="abs brand">
    <div>
      <div class="brand-name">CORVAN</div>
      <div class="brand-sub">RESOURCE CONSULTANTS LTD</div>
    </div>
    <div class="brand-mark"></div>
  </div>
  <div class="abs callus">
    <svg width="18" height="18" viewBox="0 0 18 18"><rect width="18" height="18" rx="3" fill="#333"/><path d="M6 4c-1 1-1 3 0 5s3 4 5 5c1 0 2 0 2-1l-1-2-2 1c-1-1-2-2-3-4l1-1-1-3z" fill="#fff"/></svg>
    <span>Call Us: <b>555-210-4400</b> <em>(24 Hrs)</em></span>
  </div>
  <nav class="abs nav">
    <a class="current" href="#">HOME</a><a href="#">ABOUT US</a><a href="#">SOLUTIONS</a><a href="#">TRAINING</a><a href="#">CAREERS</a><a href="#">CONTACT US</a>
  </nav>
  <div class="abs hero">
    <div class="hero-photo" role="img" aria-label="Oil field worker in hard hat and safety vest in front of pumpjacks at dusk">
      <div class="hero-title">Preparedness is the first<br>step to success.</div>
      <div class="dots"><i class="on"></i><i></i><i></i><i></i></div>
    </div>
  </div>

  <h1 class="abs">Welcome to Our Company Website</h1>
  <p class="abs intro">Corvan Resource Consultants Ltd. is an established Canadian petroleum engineering company that was founded in 1984 and is based in Calgary, Alberta. Corvan offers a variety of consulting services throughout Canada and has successfully completed projects in the United States, Europe, Africa and Asia. Corvan is actively engaged in engineering, project management and field supervision in the areas of construction, drilling and completion operations, workovers, production operations and facilities.</p>
  <a class="abs btn intro-btn" href="#">READ MORE ABOUT US</a>
  <div class="abs rule"></div>

  <div class="abs card" style="left:74px">
    <div class="card-img" role="img" aria-label="Hands placing a glowing puzzle piece" style="background:linear-gradient(135deg,#1e3a78,#5c7fc2 55,#1b2f66)"></div>
    <h2>Solutions</h2>
    <p>Corvan Resource Consultants Ltd. offers full and comprehensive service packages to our clientele.</p>
    <a class="btn" href="#">READ MORE</a>
  </div>
  <div class="abs card" style="left:344px">
    <div class="card-img" role="img" aria-label="Silhouetted workers beside a pumpjack at sunset" style="background:linear-gradient(180deg,#6b6f7a,#c9a26a 70%,#2a2520)"></div>
    <h2>Training</h2>
    <p>Corvan Resource Consultants Ltd. offers full and comprehensive service packages to our clientele.</p>
    <a class="btn" href="#">READ MORE</a>
  </div>
  <div class="abs card" style="left:614px">
    <div class="card-img" role="img" aria-label="Engineers wearing blue hard hats at work" style="background:linear-gradient(120deg,#dfe6ee,#b9c8d8 50%,#e9edf2)"></div>
    <h2>Careers</h2>
    <p>Corvan Resource Consultants Ltd. offers full and comprehensive service packages to our clientele.</p>
    <a class="btn" href="#">READ MORE</a>
  </div>

  <a class="abs tile" style="top:516px">
    <svg width="58" height="44" viewBox="0 0 58 44" fill="#fff"><circle cx="12" cy="12" r="7"/><circle cx="46" cy="12" r="7"/><circle cx="29" cy="10" r="9"/><path d="M0 34c0-8 5-12 12-12 3 0 5 1 7 2-3 3-5 6-5 10z"/><path d="M58 34c0-8-5-12-12-12-3 0-5 1-7 2 3 3 5 6 5 10z"/><path d="M12 40c0-11 7-17 17-17s17 6 17 17z"/></svg>
    <span>Public<br>Resources</span>
  </a>
  <a class="abs tile" style="top:622px">
    <svg width="58" height="58" viewBox="0 0 58 58" fill="#fff"><circle cx="29" cy="10" r="7"/><circle cx="11" cy="12" r="6"/><circle cx="47" cy="12" r="6"/><rect x="20" y="19" width="18" height="24" rx="3"/><rect x="24" y="40" width="10" height="16"/><rect x="3" y="20" width="15" height="20" rx="3"/><rect x="6" y="38" width="8" height="14"/><rect x="40" y="20" width="15" height="20" rx="3"/><rect x="44" y="38" width="8" height="14"/></svg>
    <span>Staff<br>Resources</span>
  </a>
  <a class="abs tile" style="top:728px">
    <svg width="58" height="60" viewBox="0 0 58 60" fill="none" stroke="#fff" stroke-width="3"><rect x="10" y="3" width="38" height="48" rx="3"/><path d="M18 14h22M18 22h22M18 30h10"/><circle cx="24" cy="41" r="5"/><path d="M20 45v12l4-3 4 3V45" fill="#fff"/></svg>
    <span>Certified ICS<br>Training</span>
  </a>

  <div class="abs contact">
    <h3>Contact Us</h3>
    <div class="org">Corvan Resources<br>Consultants. Ltd.</div>
    <div class="addr">410, 72 - Harwick Street SW<br>Calgary, AB T0X 1Q0</div>
    <dl>
      <dt>Tel:</dt><dd>555-210-4400 (24 Hrs)</dd>
      <dt>Fax:</dt><dd>555-210-4477 (24 Hrs)</dd>
      <dt>Email:</dt><dd>mail@corvanplan.example</dd>
    </dl>
  </div>

  <footer class="abs footer">
    <div class="foot-links">HOME<span>/</span>ABOUT US<span>/</span>SOLUTIONS<span>/</span>TRAINING<span>/</span>CAREERS<span>/</span>CONTACT US</div>
    <div class="copy">Copyright © 2014. Corvan. All Right Reserved</div>
    <div class="social">
      <i style="background:#3b5a9a"></i><i style="background:#2aa3dc"></i><i style="background:#1f7fb6"></i><i style="background:#2b2b2b"></i><i style="background:#d9231f"></i>
    </div>
  </footer>
</div>
</body>
</html>
```